Website design for new health & wellness company

We need our website to be designed in a user friendly way. Needs to be aesthetically pleasing to viewer and easy to navigate and upload content for our small team . The logo should be completely redesigned , please do not reference the current one thats on our site for a starting place. (included below though) We want to move away from that.

the website is : www.brightpathforward.com

We are a small group of writers/coaches who believe that to change the world you have to be the change and we provide tips/suggestions for every day life that if followed can make a huge difference in your life and overall being.

Target Market(s)

Men and women ages 22 to 50

Industry/Entity Type

Health And Wellness

Logo Text

Cultivate the life of your dreams

Coding

Coded - Design and coding required

Number of Pages Required

3 page

Font styles to use
Sans Serif

Colors

Designer to choose colors to be used in the design.

Requirements
Must have
• Easy to navigate. Mobile friendly. Gender neutral, should appeal to both.

```html
<!DOCTYPE html>
<html lang="en">
<head>
<meta charset="utf-8">
<title>Brightpath — Life Coaching</title>
<link href="https://fonts.googleapis.com/css2?family=Roboto:wght@300;400;500;700&display=swap" rel="stylesheet">
<style>
:root{
  --green:#8cc63f;
  --green-dark:#6fa82c;
  --purple:#6b2a8f;
  --purple-soft:#7e3aa3;
  --ink:#333842;
  --muted:#8a8f98;
  --line:#e3e5e8;
  --paper:#ffffff;
  --mist:#f3f4f6;
  --night:#2c313b;
  --night-deep:#232730;
}
*{box-sizing:border-box;margin:0;padding:0}
html,body{width:1200px;height:3300px;overflow:hidden}
body{font-family:'Roboto',sans-serif;color:var(--ink);background:var(--paper);font-size:14px;line-height:1.5}
.wrap{width:1120px;margin:0 auto;position:relative}
a{color:inherit;text-decoration:none}

/* header */
.site-header{position:absolute;top:0;left:0;width:1200px;height:46px;background:rgba(255,255,255,.92);z-index:2}
.site-header .wrap{display:flex;justify-content:space-between;align-items:center;height:46px}
.brand{display:flex;align-items:center;gap:8px;font-size:26px;font-weight:400;color:var(--green)}
.brand-dot{width:14px;height:14px;border-radius:50%;background:var(--green)}
.main-nav{display:flex;gap:0}
.main-nav a{font-size:11px;font-weight:700;letter-spacing:.5px;padding:15px 12px;color:#444}
.main-nav a.active{background:var(--green);color:#fff}

/* hero */
.hero{position:relative;height:620px;background:linear-gradient(120deg,#cfd4d8 0%,#b9aa9e 35%,#c9b6a4 55%,#e3dfdc 100%);text-align:center;color:#fff}
.hero-photo{position:absolute;inset:0;background:radial-gradient(ellipse at 50% 60%,rgba(180,130,110,.55),rgba(120,130,140,.25) 60%,rgba(90,100,110,.3))}
.hero-content{position:relative;padding-top:290px}
.hero h1{font-size:52px;font-weight:300;letter-spacing:.5px}
.hero p{width:560px;margin:12px auto 0;font-size:14px;opacity:.95}
.btn{display:inline-block;background:var(--green);color:#fff;font-size:11px;font-weight:700;letter-spacing:.5px;padding:11px 26px;border-radius:2px}
.hero .btn{margin-top:24px}
.hero-scroll{position:absolute;left:50%;bottom:28px;width:16px;height:26px;margin-left:-8px;border:2px solid #fff;border-radius:9px}

/* welcome */
.welcome{height:590px;text-align:center;padding-top:78px}
.eyebrow{font-size:12px;font-weight:500;letter-spacing:1px;color:var(--muted)}
.section-title{font-size:30px;font-weight:500;letter-spacing:.5px;color:var(--ink)}
.welcome .section-title{margin-top:4px}
.title-rule{width:220px;height:1px;background:var(--line);margin:12px auto 0;position:relative}
.title-rule::after{content:"";position:absolute;left:50%;top:-1px;width:40px;height:3px;margin-left:-20px;background:var(--green)}
.welcome .lead{width:860px;margin:20px auto 0;font-size:13px;color:#666}
.features{display:flex;justify-content:center;gap:28px;margin-top:46px}
.feature{width:240px;height:250px;padding-top:40px}
.feature.raised{background:#fff;box-shadow:0 6px 22px rgba(0,0,0,.13)}
.feature-icon{width:58px;height:58px;margin:0 auto;border-radius:50%;display:flex;align-items:center;justify-content:center}
.feature-icon.plain{background:#fff}
.feature-icon.filled{background:var(--green)}
.feature h3{font-size:14px;font-weight:700;margin-top:16px;letter-spacing:.3px}
.feature p{font-size:11px;color:var(--muted);width:180px;margin:8px auto 0}
.read-more{display:inline-block;margin-top:14px;font-size:10px;font-weight:700;color:var(--purple)}
.feature.raised .read-more{color:var(--green)}

/* purple coaching */
.coaching{height:570px;background:var(--purple);padding-top:80px;text-align:center}
.coaching .section-title{color:#fff}
.coaching .title-rule{background:rgba(255,255,255,.3)}
.cards{display:flex;justify-content:center;gap:38px;margin-top:50px}
.card{width:328px;height:348px;background:#fff;text-align:left}
.card-photo{height:188px}
.photo-a{background:linear-gradient(135deg,#c8ccd2,#5b6470 60%,#2f3640)}
.photo-b{background:linear-gradient(135deg,#e8e1dc,#c2413f 45%,#8a6b58)}
.photo-c{background:linear-gradient(135deg,#f1f2f3,#b9c6cf 50%,#dad3cc)}
.card-body{padding:24px 24px}
.card h3{font-size:13px;font-weight:700;letter-spacing:.3px}
.card p{font-size:11px;color:var(--muted);margin-top:8px}

/* areas */
.areas{height:340px;background:var(--mist);padding-top:104px;text-align:center}
.area-list{display:flex;justify-content:center;gap:60px;margin-top:52px}
.area{display:flex;align-items:flex-start;gap:18px;width:310px;text-align:left}
.area-icon{flex:none;width:70px;height:70px;border-radius:50%;display:flex;align-items:center;justify-content:center;background:#fff}
.area-icon.active{background:var(--green)}
.area h3{font-size:13px;font-weight:700;line-height:1.25;margin-top:6px}
.area p{font-size:11px;color:var(--muted);margin-top:6px}

/* testimonials */
.testimonials{height:440px;padding-top:110px;text-align:center}
.avatars{display:flex;justify-content:center;align-items:center;gap:6px;margin-top:30px}
.avatar{border-radius:50%;background:linear-gradient(135deg,#d9c7b6,#8d7766)}
.avatar.small{width:44px;height:44px;opacity:.7}
.avatar.main{width:70px;height:70px;border:3px solid var(--green)}
.quote{width:780px;margin:30px auto 0;font-size:13px;color:#666;position:relative}
.quote-arrow{position:absolute;top:10px;font-size:20px;color:var(--muted)}
.quote-arrow.prev{left:-50px}.quote-arrow.next{right:-50px}
.quote-author{margin-top:14px;font-size:11px;font-weight:700}
.dots{display:flex;justify-content:center;gap:8px;margin-top:20px}
.dots span{width:8px;height:8px;border-radius:50%;background:#ccc}
.dots span.on{background:var(--green)}

/* events */
.events{height:400px;background:var(--green);padding-top:78px;color:#fff}
.events .section-title{color:#fff;text-align:center}
.events .title-rule{background:rgba(255,255,255,.4)}
.events .title-rule::after{background:#fff}
.slider-arrows{position:absolute;right:20px;top:6px;display:flex;gap:14px;font-size:20px}
.event-list{display:flex;gap:40px;margin-top:60px;padding-left:0}
.event{width:346px}
.event-date{display:flex;align-items:center;gap:8px;font-size:11px;font-weight:500}
.event h3{font-size:14px;font-weight:700;margin-top:4px}
.event p{font-size:11px;margin-top:6px;opacity:.9}
.event .read-more{color:#fff}

/* footer */
.site-footer{height:340px;background:var(--night);color:#b4b8bf;position:relative}
.footer-grid{display:flex;padding-top:52px}
.footer-about{width:392px}
.footer-about .brand{color:var(--green)}
.footer-about p{font-size:11px;margin-top:22px;width:250px}
.footer-col{width:180px}
.footer-col h4{font-size:11px;font-weight:700;color:#fff;letter-spacing:.5px}
.footer-col ul{list-style:none;margin-top:12px}
.footer-col li{font-size:11px;line-height:22px;display:flex;align-items:center;gap:8px}
.bullet{width:8px;height:8px;border-radius:50%;background:var(--green);flex:none}
.footer-contact{width:260px}
.footer-bar{position:absolute;left:0;bottom:0;width:1200px;height:50px;background:var(--night-deep)}
.footer-bar .wrap{display:flex;justify-content:space-between;align-items:center;height:50px;font-size:11px}
.to-top{position:absolute;right:6px;bottom:62px;width:26px;height:26px;border-radius:50%;background:var(--purple)}
</style>
</head>
<body>

<header class="site-header">
  <div class="wrap">
    <a class="brand" href="#"><span class="brand-dot"></span>Brightpath</a>
    <nav class="main-nav">
      <a class="active" href="#">HOME</a>
      <a href="#">ABOUT</a>
      <a href="#">TRAINING</a>
      <a href="#">CHANGES</a>
      <a href="#">BLOG</a>
      <a href="#">CONTACTS</a>
    </nav>
  </div>
</header>

<section class="hero">
  <div class="hero-photo" role="img" aria-label="Photo of a smiling mother and daughter at home"></div>
  <div class="hero-content">
    <h1>You can live a better life</h1>
    <p>Lorem ipsum dolor sit amet, consectetuer adipiscing elit. Aenean commodo ligula eget dolor, aenean massa cum sociis.</p>
    <a class="btn" href="#">START TODAY</a>
  </div>
  <span class="hero-scroll"></span>
</section>

<section class="welcome">
  <div class="eyebrow">WELCOME TO</div>
  <h2 class="section-title">BRIGHT PATH FORWARD</h2>
  <div class="title-rule"></div>
  <p class="lead">Lorem ipsum dolor sit amet, consectetuer adipiscing elit. Aenean commodo ligula eget dolor. Cum sociis natoque penatibus et magnis dis parturient montes, nascetur ridiculus mus. Donec quam felis, ultricies nec pellentesque eu.</p>
  <div class="features">
    <div class="feature">
      <div class="feature-icon plain"><svg width="30" height="30" viewBox="0 0 30 30"><rect x="4" y="10" width="22" height="15" rx="2" fill="var(--purple)"/><rect x="11" y="6" width="8" height="5" rx="1" fill="none" stroke="var(--purple)" stroke-width="2"/></svg></div>
      <h3>WORK &amp; CAREER</h3>
      <p>Lorem ipsum dolor sit amet, consectetuer adipiscing.</p>
      <a class="read-more" href="#">READ MORE</a>
    </div>
    <div class="feature raised">
      <div class="feature-icon filled"><svg width="30" height="30" viewBox="0 0 30 30"><text x="15" y="22" text-anchor="middle" font-family="Roboto,sans-serif" font-size="20" font-weight="700" fill="#fff">$</text></svg></div>
      <h3>MONEY &amp; FINANCE</h3>
      <p>Lorem ipsum dolor sit amet, consectetuer adipiscing.</p>
      <a class="read-more" href="#">READ MORE</a>
    </div>
    <div class="feature">
      <div class="feature-icon plain"><svg width="30" height="30" viewBox="0 0 30 30"><path d="M9 5h12v7a6 6 0 0 1-12 0z" fill="var(--purple)"/><rect x="13" y="18" width="4" height="5" fill="var(--purple)"/><rect x="9" y="23" width="12" height="3" fill="var(--purple)"/></svg></div>
      <h3>LIFE &amp; LIVING</h3>
      <p>Lorem ipsum dolor sit amet, consectetuer adipiscing.</p>
      <a class="read-more" href="#">READ MORE</a>
    </div>
    <div class="feature">
      <div class="feature-icon plain"><svg width="30" height="30" viewBox="0 0 30 30"><path d="M15 5c6 0 11 4 11 9s-5 9-11 9c-1 0-2 0-3-.3L6 25l2-5c-2-1.6-4-3.7-4-6 0-5 5-9 11-9z" fill="var(--purple)"/></svg></div>
      <h3>DISCUSSIONS</h3>
      <p>Lorem ipsum dolor sit amet, consectetuer adipiscing.</p>
      <a class="read-more" href="#">READ MORE</a>
    </div>
  </div>
</section>

<section class="coaching">
  <h2 class="section-title">WHAT CAN LIFE COACHING DO FOR YOU?</h2>
  <div class="title-rule"></div>
  <div class="cards">
    <article class="card">
      <div class="card-photo photo-a" role="img" aria-label="Photo of a businessman in a suit"></div>
      <div class="card-body"><h3>CONSECTETUER ADIPISCING</h3><p>Nam quam nunc blandit vel luctus pulvinar, hendrerit id lorem maecenas nec odio et ante tincidunt tempus donec.</p></div>
    </article>
    <article class="card">
      <div class="card-photo photo-b" role="img" aria-label="Photo of two women working together at a desk"></div>
      <div class="card-body"><h3>CONSECTETUER ADIPISCING</h3><p>Nam quam nunc blandit vel luctus pulvinar, hendrerit id lorem maecenas nec odio et ante tincidunt tempus donec.</p></div>
    </article>
    <article class="card">
      <div class="card-photo photo-c" role="img" aria-label="Photo of a doctor talking with an older patient"></div>
      <div class="card-body"><h3>CONSECTETUER ADIPISCING</h3><p>Nam quam nunc blandit vel luctus pulvinar, hendrerit id lorem maecenas nec odio et ante tincidunt tempus donec.</p></div>
    </article>
  </div>
</section>

<section class="areas">
  <h2 class="section-title">LIFE COACHING AREAS</h2>
  <div class="title-rule"></div>
  <div class="area-list">
    <div class="area">
      <div class="area-icon active"><svg width="30" height="30" viewBox="0 0 30 30"><circle cx="11" cy="11" r="4" fill="#fff"/><circle cx="20" cy="11" r="4" fill="#fff"/><path d="M4 24c0-5 3-8 7-8s7 3 7 8zM14 24c0-5 2-8 6-8s6 3 6 8z" fill="#fff"/></svg></div>
      <div><h3>RELATIONSHIP<br>COACHING</h3><p>Lorem ipsum dolor sit amet, cursus consectetuer adipiscing elit dolor.</p></div>
    </div>
    <div class="area">
      <div class="area-icon"><svg width="30" height="30" viewBox="0 0 30 30"><rect x="5" y="9" width="20" height="13" rx="2" fill="none" stroke="#b9bdc4" stroke-width="2"/><circle cx="15" cy="15.5" r="3" fill="#b9bdc4"/></svg></div>
      <div><h3>FINANCIAL<br>COACHING</h3><p>Lorem ipsum dolor sit amet, cursus consectetuer adipiscing elit dolor.</p></div>
    </div>
    <div class="area">
      <div class="area-icon"><svg width="30" height="30" viewBox="0 0 30 30"><path d="M6 8h14v10H11l-5 4z" fill="none" stroke="#b9bdc4" stroke-width="2"/><path d="M22 12h3v10l-4-3h-8" fill="none" stroke="#b9bdc4" stroke-width="2"/></svg></div>
      <div><h3>EXECUTIVE<br>COACHING</h3><p>Lorem ipsum dolor sit amet, cursus consectetuer adipiscing elit dolor.</p></div>
    </div>
  </div>
</section>

<section class="testimonials">
  <h2 class="section-title">TESTIMONIALS</h2>
  <div class="title-rule"></div>
  <div class="avatars">
    <div class="avatar small" role="img" aria-label="Client portrait"></div>
    <div class="avatar main" role="img" aria-label="Portrait of the quoted client"></div>
    <div class="avatar small" role="img" aria-label="Client portrait"></div>
  </div>
  <div class="quote">
    <span class="quote-arrow prev">&lsaquo;</span>
    <p>Lorem ipsum dolor sit amet, consectetuer adipiscing elit. Aenean commodo ligula eget dolor. Cum sociis natoque magnis dis parturient montes nascetur ridiculus mus, donec quam felis ultricies nec pellentesque.</p>
    <span class="quote-arrow next">&rsaquo;</span>
    <div class="quote-author">— Practice Family Provider</div>
  </div>
  <div class="dots"><span class="on"></span><span></span></div>
</section>

<section class="events">
  <div class="wrap">
    <h2 class="section-title">PUBLIC EVENTS</h2>
    <div class="title-rule"></div>
    <div class="slider-arrows"><span>&lsaquo;</span><span>&rsaquo;</span></div>
    <div class="event-list">
      <div class="event">
        <div class="event-date"><svg width="12" height="12" viewBox="0 0 12 12"><rect x="1" y="2" width="10" height="9" fill="none" stroke="#fff" stroke-width="1.4"/><line x1="1" y1="5" x2="11" y2="5" stroke="#fff" stroke-width="1.4"/></svg>OCT 18</div>
        <h3>CONSECTETUER ADIPISCING</h3>
        <p>Lorem ipsum dolor sit amet, consectetuer adipiscing elit sed do eiusmod tempor incididunt ut labore dolore magna.</p>
        <a class="read-more" href="#">READ MORE</a>
      </div>
      <div class="event">
        <div class="event-date"><svg width="12" height="12" viewBox="0 0 12 12"><rect x="1" y="2" width="10" height="9" fill="none" stroke="#fff" stroke-width="1.4"/><line x1="1" y1="5" x2="11" y2="5" stroke="#fff" stroke-width="1.4"/></svg>OCT 22</div>
        <h3>CONSECTETUER ADIPISCING</h3>
        <p>Lorem ipsum dolor sit amet, consectetuer adipiscing elit sed do eiusmod tempor incididunt ut labore dolore magna.</p>
        <a class="read-more" href="#">READ MORE</a>
      </div>
      <div class="event">
        <div class="event-date"><svg width="12" height="12" viewBox="0 0 12 12"><rect x="1" y="2" width="10" height="9" fill="none" stroke="#fff" stroke-width="1.4"/><line x1="1" y1="5" x2="11" y2="5" stroke="#fff" stroke-width="1.4"/></svg>OCT 29</div>
        <h3>CONSECTETUER ADIPISCING</h3>
        <p>Lorem ipsum dolor sit amet, consectetuer adipiscing elit sed do eiusmod tempor incididunt ut labore dolore magna.</p>
        <a class="read-more" href="#">READ MORE</a>
      </div>
    </div>
  </div>
</section>

<footer class="site-footer">
  <div class="wrap footer-grid">
    <div class="footer-about">
      <a class="brand" href="#"><span class="brand-dot"></span>Brightpath</a>
      <p>Lorem ipsum dolor sit amet, consectetuer adipiscing elit. Aenean commodo ligula eget dolor cum sociis natoque penatibus magnis dis parturient.</p>
    </div>
    <div class="footer-col">
      <h4>COMPANY</h4>
      <ul><li>Coaching</li><li>Workshops</li><li>Articles</li><li>Our Staff</li><li>Contacts</li><li>Blog</li></ul>
    </div>
    <div class="footer-col">
      <h4>FOLLOW US</h4>
      <ul><li><span class="bullet"></span>Community</li><li><span class="bullet"></span>Updates</li><li><span class="bullet"></span>Circle</li><li><span class="bullet"></span>Network</li><li><span class="bullet"></span>Newsletter</li></ul>
    </div>
    <div class="footer-col footer-contact">
      <h4>CONTACT US</h4>
      <ul>
        <li><svg width="10" height="10" viewBox="0 0 10 10"><path d="M2 1l2 2-1 1.5c.8 1.3 1.7 2.2 3 3L7.5 6l2 2L8 9.5C4.5 9 1 5.5.5 2z" fill="var(--green)"/></svg>Telephone: +1 555 014 288</li>
        <li><svg width="10" height="10" viewBox="0 0 10 10"><rect x="1" y="2" width="8" height="6" fill="var(--green)"/></svg>Fax: +1 555 014 289</li>
        <li><svg width="10" height="10" viewBox="0 0 10 10"><rect x="1" y="2" width="8" height="6" fill="none" stroke="var(--green)"/><path d="M1 2l4 3 4-3" fill="none" stroke="var(--green)"/></svg>E-mail: hello@brightpathforward.com</li>
      </ul>
    </div>
  </div>
  <div class="footer-bar">
    <div class="wrap"><span>Copyright © 2017 | All Right Reserved</span><span>Terms &amp; Conditions | Privacy Policy</span></div>
  </div>
  <span class="to-top"></span>
</footer>

</body>
</html>
```